New Property development signage

large poster for a new development.
3 metres x 2 metres. To include the following.

Varnock Meadows
TO LET
LUXURY FULLY FURNISHED LARGE
2 AND 3 BED APARTMENTS
Tilwick Estates
362 4159
www.tilwickestates-example.com

Need this to be large simple writing with Tilwick estates logo on the bottom

Target Market(s)

High end rental property market

Industry/Entity Type

Real Estate Development

Colors
000000
cbcbcb
0555a3

Requirements
Must have
• Name of the development must be in a different font, classic style
Nice to have
• Light Grey background, blues for colours
Should not have
• anymore than 3 /4 colours

```html
<!DOCTYPE html>
<html lang="en">
<head>
<meta charset="utf-8">
<title>Varnock Meadows – To Let</title>
<link rel="stylesheet" href="https://fonts.googleapis.com/css2?family=Cinzel:wght@400;600;700&family=Cormorant+Garamond:wght@400&family=EB+Garamond:wght@700&display=swap">
<style>
  :root {
    --bg-grey: #b4b4b6;
    --panel-blue: #233b8b;
    --accent-orange: #e8591c;
    --ink: #262626;
    --white: #ffffff;
  }
  html, body {
    margin: 0;
    padding: 0;
    width: 1200px;
    height: 804px;
    overflow: hidden;
    background: var(--bg-grey);
  }
  .sign {
    position: relative;
    width: 1200px;
    height: 804px;
    background: var(--bg-grey);
  }
  .headline-panel {
    position: absolute;
    left: 18px;
    top: 20px;
    width: 1167px;
    height: 537px;
    background: var(--panel-blue);
    box-shadow: 4px 5px 8px rgba(0,0,0,0.35);
    color: var(--white);
    text-align: center;
    font-family: "Cinzel", serif;
  }
  .development-name {
    position: absolute;
    left: 0; right: 0;
    top: 140px;
    margin: 0;
    font-weight: 400;
    font-size: 43px;
    letter-spacing: 3px;
  }
  .offer {
    position: absolute;
    left: 0; right: 0;
    margin: 0;
    font-weight: 700;
    white-space: nowrap;
  }
  .offer-line-1 { top: 262px; font-size: 57px; letter-spacing: 1px; }
  .offer-line-2 { top: 360px; font-size: 72px; letter-spacing: 2px; }

  .agent-badge {
    position: absolute;
    left: 89px;
    top: 582px;
    width: 420px;
    height: 195px;
    background: var(--panel-blue);
    color: var(--white);
    font-family: "Cinzel", serif;
  }
  .agent-name {
    position: absolute;
    left: 0; right: 0;
    top: 40px;
    margin: 0;
    text-align: center;
    font-weight: 700;
    font-size: 48px;
    line-height: 1;
  }
  .agent-services {
    position: absolute;
    left: 0; right: 0; bottom: 0;
    height: 38px;
    background: var(--accent-orange);
    font-family: "EB Garamond", serif;
    font-weight: 700;
    font-size: 19px;
    line-height: 38px;
    text-align: center;
  }
  .contact {
    position: absolute;
    left: 600px;
    top: 615px;
    width: 530px;
    text-align: center;
    color: var(--ink);
  }
  .contact-phone {
    margin: 0;
    font-family: "Cormorant Garamond", serif;
    font-weight: 400;
    font-size: 104px;
    line-height: 0.9;
    letter-spacing: 5px;
  }
  .contact-web {
    margin: 6px 0 0;
    font-family: "EB Garamond", serif;
    font-weight: 700;
    font-size: 27px;
    letter-spacing: 0.5px;
  }
</style>
</head>
<body>
  <main class="sign">
    <section class="headline-panel">
      <h1 class="development-name">VARNOCK MEADOWS TO LET</h1>
      <p class="offer offer-line-1">LUXURY FULLY FURNISHED LARGE</p>
      <p class="offer offer-line-2">2 AND 3 BED APARTMENTS</p>
    </section>

    <div class="agent-badge">
      <p class="agent-name">Tilwick<br>Estates</p>
      <div class="agent-services">Sales • Lettings • Management • B.E.R. Certs</div>
    </div>

    <div class="contact">
      <p class="contact-phone">362 4159</p>
      <p class="contact-web">www.tilwickestates-example.com</p>
    </div>
  </main>
</body>
</html>
```